Clean, Fresh Business Card Design Needed

We need a business card design for a new business we have taken over called "Bonders and Fixers". We got a logo through this website which i have attached. We are wanting something that is vibrant but clean and fresh. Our business mainly sells glue. Maybe a cool design/slogan on the back? Modern, sleek.

Industry/Entity Type

Business

Contact Information for Business Card

Name: Derek Tamsin, Managing Director. Address: 164 Kowhai Lane, Tauranga 3112, Phone: 07 549 2361 Mobile: 021 634 915 Fax: 07 549 2874 Email: bond.fix@mailvo.co.nz, Web: www.tackbondpro.co.nz

Font styles to use
Serif

Requirements
Must have
• All business card details, logo.
Nice to have
• Design, slogan on back of card

```html
<!DOCTYPE html>
<html lang="en">
<head>
<meta charset="utf-8">
<title>Bonders and Fixers – Business Card</title>
<link rel="stylesheet" href="https://fonts.googleapis.com/css2?family=Cinzel:wght@400&family=Arimo:wght@400;700&display=swap">
<style>
  :root {
    --brand-blue: #3848a8;
    --brand-blue-dark: #2e3c94;
    --paper: #ffffff;
    --ink: #1d1d1f;
    --stage: #e8e5e0;
  }
  * { box-sizing: border-box; margin: 0; padding: 0; }
  html, body { width: 1200px; height: 858px; overflow: hidden; }
  body {
    background: var(--stage);
    display: flex;
    align-items: center;
    justify-content: center;
    gap: 40px;
    font-family: "Arimo", Arial, sans-serif;
  }
  .card {
    position: relative;
    width: 540px;
    height: 309px;
    overflow: hidden;
    box-shadow: 0 6px 18px rgba(0,0,0,.18);
  }

  /* ---------- Front ---------- */
  .card--front { background: var(--paper); }
  .front__band {
    position: absolute; left: 0; top: 0; bottom: 0;
    width: 54px;
    background: var(--brand-blue);
  }
  .front__band::after {
    content: ""; position: absolute; top: 0; bottom: 0; right: 4px;
    border-right: 1.5px solid var(--paper);
  }
  .brand-mark {
    position: absolute;
    background: var(--paper);
    border: 4px solid var(--brand-blue);
    border-radius: 10px;
  }
  .card--front .brand-mark { left: 14px; top: 34px; width: 82px; height: 82px; box-shadow: 0 0 0 2px var(--paper); }
  .brand-name {
    position: absolute;
    font-family: "Cinzel", "Times New Roman", serif;
    font-weight: 400;
    line-height: 1.05;
    text-transform: uppercase;
  }
  .card--front .brand-name { left: 112px; top: 42px; font-size: 34px; color: var(--ink); }
  .brand-name .line2 { display: block; letter-spacing: .12em; }

  .person { position: absolute; right: 40px; top: 142px; text-align: left; }
  .person__name { font-weight: 700; font-size: 21px; color: var(--ink); letter-spacing: -.01em; }
  .person__title { font-size: 14px; color: var(--brand-blue); margin-top: 1px; }
  .person__rule {
    position: absolute; left: 330px; right: 0; top: 196px;
    border-top: 1.2px solid var(--brand-blue);
  }

  .contact-list { position: absolute; list-style: none; font-size: 11.5px; color: var(--ink); }
  .contact-list li { display: flex; align-items: center; gap: 7px; height: 19px; }
  .contact-list--web { left: 334px; top: 208px; }
  .contact-list--phone { left: 132px; top: 222px; }
  .icon {
    width: 14px; height: 14px; flex: none;
    background: var(--brand-blue); border-radius: 2px;
    display: flex; align-items: center; justify-content: center;
  }
  .icon svg { width: 10px; height: 10px; fill: none; stroke: var(--paper); stroke-width: 1.4; }

  /* ---------- Back ---------- */
  .card--back { background: linear-gradient(135deg, var(--brand-blue) 0%, var(--brand-blue-dark) 100%); }
  .back__lockup {
    position: absolute; inset: 0;
    display: flex; align-items: center; justify-content: center; gap: 22px;
  }
  .card--back .brand-mark {
    position: static; width: 96px; height: 96px;
    border: none; border-radius: 12px;
  }
  .card--back .brand-name { position: static; font-size: 40px; color: var(--paper); }
</style>
</head>
<body>

  <section class="card card--front" aria-label="Business card front">
    <div class="front__band"></div>
    <div class="brand-mark" aria-hidden="true"></div>
    <div class="brand-name">Bonders<span class="line2">and Fixers</span></div>

    <div class="person">
      <div class="person__name">Derek Tamsin</div>
      <div class="person__title">Manager</div>
    </div>
    <div class="person__rule"></div>

    <ul class="contact-list contact-list--web">
      <li><span class="icon"><svg viewBox="0 0 10 10"><rect x="1" y="2" width="8" height="6"/><path d="M1 2l4 3.5L9 2"/></svg></span>bond.fix@mailvo.co.nz</li>
      <li><span class="icon"><svg viewBox="0 0 10 10"><circle cx="5" cy="5" r="4"/><path d="M1 5h8M5 1c-2 2.5-2 5.5 0 8M5 1c2 2.5 2 5.5 0 8"/></svg></span>www.tackbondpro.co.nz</li>
      <li><span class="icon"><svg viewBox="0 0 10 10"><path d="M5 9C2.5 6 2 4.8 2 4a3 3 0 0 1 6 0c0 .8-.5 2-3 5z"/><circle cx="5" cy="4" r="1"/></svg></span>164 Kowhai Lane, Tauranga 3112</li>
    </ul>

    <ul class="contact-list contact-list--phone">
      <li><span class="icon"><svg viewBox="0 0 10 10"><path d="M2 1.5l2 .2.6 2-1.2.9a5 5 0 0 0 2 2l.9-1.2 2 .6.2 2C7 8.8 4.5 8.5 3 7S1.2 3 2 1.5z"/></svg></span>07 549 2361</li>
      <li><span class="icon"><svg viewBox="0 0 10 10"><rect x="3" y="1" width="4" height="8" rx=".6"/><path d="M4.5 7.5h1"/></svg></span>021 634 915</li>
      <li><span class="icon"><svg viewBox="0 0 10 10"><rect x="1.5" y="4" width="7" height="4"/><path d="M3 4V1.5h4V4M3 6.5h4"/></svg></span>07 549 2874</li>
    </ul>
  </section>

  <section class="card card--back" aria-label="Business card back">
    <div class="back__lockup">
      <div class="brand-mark" aria-hidden="true"></div>
      <div class="brand-name">Bonders<span class="line2">and Fixers</span></div>
    </div>
  </section>

</body>
</html>
```